Football (soccer) board game app design

Hi,

We are a start up looking for a gameplay design for an app. It is a football trivia app that consists of four main screens; login/register, main navigation, gameplay, question.

OVERALL:
We want our app to be kept in a dark theme. Black or very dark gray is preferable, with a couple of nice colors to give it a stylish touch. We like flat designs, but are open for ideas within the general structure design. The logo can be used in the app, but feel free to improve it you feel you can. In the attached material we have tried to outline some of our ideas and other designs friends have helped us make.

LOGIN/REGISTER:
We want a simple login. Email, password, Linkora login and the possibility to register a new user. Live search check whether the email is valid and free, and there is also live validation of passwords. If this could be incorporated in the design it would be nice.

MAIN NAVIGATION:
In the main navigation screen we want it to be divided into tabs. A home, my games, my categories and a ranking tab. In the top bar it should be possible to search for categories as well as there should be a button to go to settings.

The Home tab
In the home tab we want a "Quick Play" button, and a list of featured categories. A category can be unlocked or locked, which should be illustrated somehow. When a category is tapped it should divide the block into a left and right tap area, where the user can choose to "Beat to unlock" or "Buy to unlock" if locked and "Practice" or "Challenge Friend" if already unlocked.

The My Games tab
In the my games tab, the current games should be divided into three lists. First "your turn", then "opponents turn" and finally "finished games".

The My Categories tab
This tab should include a list of categories, which the user have bought, but as of design it is fairly similar to the blocks in home tab. So not much different here.

The Ranking tab
Ranking should show a set of leaderboards; Today, This Week, This Month, etc. The row in a leaderboard should have teamname and a win percentage.

GAMEPLAY:
The gameplay is inspired by an old football (soccer) board game from the 1950's, and our gameplay consists of three core elements; a football (soccer) pitch, 11 players and a scoreboard.

The football (soccer) pitch
What we need is a pitch seen from behind the goal line. The important issue here, is the perspective, as we want 11 players on the field formed as a 4-3-3 formation, being 1 goalkeeper, 4 defenders, 3 midfielder and 3 strikers. They should all be touchable without overlap. In the other end we want a goal that should be touchable as well. The goal in the nearest end do not have to be visible. Due to the perspective of the field and the fact that players and goal should be touchable, of course give you the opportunity to play around with the proportions of both players and goal. We rather want a large goal being out of proportions, than a small goal with a tiny tap area. Around the field (sidelines and beside the goal) we would like advertising banners like seen on a real stadium.

The players
As mentioned we want 11 players in a 4-3-3 formation. The players should be attached to the board with springs as seen on some of the very old board games, where you could flick the player to pass the ball. This also means that we want the players to be placed in an indentation for the ball to fall into and it would be very cool if you could illustrate the player with the ball, as being pulled back to one of the sides, just enough to see the ball at his feet. The players should be large enough for a user to tap them, hence it would also be beneficial if they are not overlapping. For a start we would like to see the players in a blue shirt and white shorts (socks are not necessary as they are placed on a spring).

Scoreboard
On the scoreboard above the field, we need information such as the names of the two teams (could be FC Brightcrest and Red Oak Rovers), the score (2-1), minutes played (42), and which half (1st). We also want a progress bar that illustrates how many moves you have used ranging from 0-5. The scoreboard could be inspired from the ones seen around stadiums across the world, but feel free to improvise.

What We Are Looking for
We are looking for full PSD and AI files so we can use them to make minor changes like colors on shirts and shorts, colors on pitch, etc. We really want you to be innovative and inspire us, as we are not designers ourselves. In the attached files, we have tried to sketch out a design that covers our initial ideas. We are looking for a professional look, and having the players and field look like a real board game would just be awesome. A combination of the look from the realistic pitch with advertising banners around it, the idea of our spring-players and the initial thoughts of a design illustrated in our sketch, should help you along. Flat design, cartoonish or somewhere in between is up to you, we just want you to impress and make "wow"-feeling.

QUESTION:
The final screen should display a question with four possible answers. There should be a green/checkmark when correct answer, and a red/cross if incorrect.

That's all. We are looking very much forward to see your designs!
Updates

Hi all,

We have changed the terms of the contest to now have a guaranteed payment, and we are really looking forward to see your designs! Good luck.

/ Mattias and Anders

By request we have now uploaded an AI-file with the logo for you to play around with. We are looking forward to see your designs.

/ Mattias and Anders

Project Deadline Extended
Reason: Hi designers, We are really happy with the progress being made, and are looking forward to see some of the designs that are still work in progress. However the amount of designs received, has not reached our expectations yet. Therefore we are extending the deadline for seven more days, so designers, that are still working on their designs can continue their work without a stressing deadline in the horizon. Good luck to all of you. We are looking very much forward to see, what you are able to produce. Best regards, Mattias and Anders

Project Deadline Extended
Reason: Hi all, We still have a lot of designers in the competition , who are battling to finish their designs, therefore we have decided to extend the deadline once more. Good luck to all of you!

Target Market(s)

Football (soccer) fans

Industry/Entity Type

Advertising

```html
<!DOCTYPE html>
<html lang="en">
<head>
<meta charset="utf-8">
<title>goalminded – login screens</title>
<link href="https://fonts.googleapis.com/css2?family=Arimo:wght@400;700&family=Raleway:wght@200&display=swap" rel="stylesheet">
<style>
  :root {
    --page: #ffffff;
    --status-bar: #2e2e2e;
    --status-text: #e6e6e6;
    --field-bg: #161616;
    --field-text: #8a8a8a;
    --icon: #4a4a4a;
    --welcome: #7a7a7a;
    --button: #3e5a86;
    --button-mark: #1f2f4f;
    --button-text: #ffffff;
    --logo: #f2f2f2;
    --check-ring: #3a3a3a;
    --check-core: #222222;
  }
  * { box-sizing: border-box; margin: 0; padding: 0; }
  html, body { width: 1200px; height: 608px; overflow: hidden; background: var(--page); }
  .board {
    position: relative; width: 1125px; height: 570px;
    transform: scale(1.0667); transform-origin: 0 0;
    font-family: "Arimo", Arial, sans-serif;
  }
  .screen { position: absolute; top: 46px; width: 320px; height: 480px; overflow: hidden; }
  .screen--email { left: 40px; }
  .screen--register { left: 396px; }
  .screen--login { left: 762px; }
  .backdrop {
    position: absolute; inset: 0;
    background:
      radial-gradient(ellipse 45% 25% at 35% 82%, rgba(110,110,110,.22), transparent 70%),
      linear-gradient(180deg, #363636 0%, #3e3e3e 35%, #383838 65%, #323232 100%);
  }
  .status-bar {
    position: absolute; top: 0; left: 0; right: 0; height: 21px;
    background: var(--status-bar); color: var(--status-text);
    font-size: 13px; font-weight: 700; text-align: center; line-height: 21px;
  }
  .status-bar .signal { position: absolute; left: 5px; top: 6px; }
  .status-bar .battery { position: absolute; right: 6px; top: 6px; }
  .wordmark {
    position: absolute; top: 44px; left: 0; right: 0; text-align: center;
    font-family: "Raleway", Arial, sans-serif; font-weight: 200;
    font-size: 42px; line-height: 48px; color: var(--logo);
  }
  .welcome {
    position: absolute; left: 0; right: 0; text-align: center;
    font-size: 18px; line-height: 22px; color: var(--welcome);
  }
  .field {
    position: absolute; height: 40px; background: var(--field-bg);
    border-radius: 2px; color: var(--field-text); font-size: 14px;
    line-height: 40px; padding-left: 53px; white-space: nowrap;
  }
  .field svg { position: absolute; left: 8px; top: 8px; }
  .field .key { left: 11px; top: 6px; }
  .check {
    position: absolute; border-radius: 50%; background: var(--check-ring);
    display: flex; align-items: center; justify-content: center;
  }
  .check span {
    width: 76%; height: 76%; border-radius: 50%; background: var(--check-core);
    display: flex; align-items: center; justify-content: center;
  }
  .login-button {
    position: absolute; left: 57px; top: 408px; width: 207px; height: 37px;
    background: var(--button); border-radius: 2px; white-space: nowrap;
    color: var(--button-text); font-size: 14px; line-height: 37px; padding-left: 50px;
  }
  .login-button .mark {
    position: absolute; left: 8px; top: 5px; width: 27px; height: 27px;
    background: var(--button-mark); border-radius: 2px;
  }
  .ground-line { position: absolute; left: 0; right: 0; top: 446px; height: 1px; background: rgba(255,255,255,.08); }
</style>
</head>
<body>
<svg width="0" height="0" style="position:absolute">
  <defs>
    <symbol id="icon-mail" viewBox="0 0 28 22">
      <rect x="1" y="1" width="26" height="20" fill="none" stroke="#4a4a4a" stroke-width="2"/>
      <path d="M1 2 L14 13 L27 2 M1 20 L11 11 M27 20 L17 11" fill="none" stroke="#4a4a4a" stroke-width="2"/>
    </symbol>
    <symbol id="icon-key" viewBox="0 0 16 26">
      <circle cx="8" cy="7" r="6.5" fill="#4a4a4a"/>
      <circle cx="8" cy="6" r="2" fill="#161616"/>
      <rect x="6" y="12" width="4" height="13" fill="#4a4a4a"/>
      <rect x="10" y="18" width="3" height="2" fill="#4a4a4a"/>
    </symbol>
    <symbol id="icon-tick" viewBox="0 0 30 26">
      <path d="M3 14 L11 22 L27 3" fill="none" stroke="#9a9a9a" stroke-width="5" stroke-linejoin="round" stroke-linecap="round"/>
    </symbol>
    <symbol id="icon-signal" viewBox="0 0 20 8">
      <rect x="0" y="5" width="3" height="3" fill="#ddd"/><rect x="4" y="4" width="3" height="4" fill="#ddd"/><rect x="8" y="3" width="3" height="5" fill="#ddd"/><rect x="12" y="1" width="3" height="7" fill="#ddd"/><rect x="16" y="0" width="3" height="8" fill="#ddd"/>
    </symbol>
    <symbol id="icon-battery" viewBox="0 0 20 9">
      <rect x="0.5" y="0.5" width="16" height="8" fill="none" stroke="#ddd"/><rect x="2" y="2" width="13" height="5" fill="#ddd"/><rect x="17" y="3" width="2" height="3" fill="#ddd"/>
    </symbol>
  </defs>
</svg>

<main class="board">

  <section class="screen screen--email">
    <div class="backdrop" role="img" aria-label="Dim photo of a football pitch with a player kicking"></div>
    <header class="status-bar">
      <svg class="signal" width="20" height="8"><use href="#icon-signal"/></svg>
      9:00 AM
      <svg class="battery" width="20" height="9"><use href="#icon-battery"/></svg>
    </header>
    <div class="wordmark">goalminded</div>
    <div class="field" style="left:13px;top:227px;width:295px;">
      <svg width="28" height="24"><use href="#icon-mail"/></svg>
    </div>
    <div class="ground-line"></div>
    <div class="login-button"><span class="mark"></span>Login with Linkora</div>
  </section>

  <section class="screen screen--register">
    <div class="backdrop" role="img" aria-label="Dim photo of a football pitch with a player kicking"></div>
    <header class="status-bar">
      <svg class="signal" width="20" height="8"><use href="#icon-signal"/></svg>
      9:00 AM
      <svg class="battery" width="20" height="9"><use href="#icon-battery"/></svg>
    </header>
    <div class="wordmark">goalminded</div>
    <div class="welcome" style="top:161px;">Welcome</div>
    <div class="field" style="left:18px;top:193px;width:265px;">
      <svg width="28" height="24"><use href="#icon-mail"/></svg>anders@postvik.com
    </div>
    <div class="field" style="left:18px;top:238px;width:265px;">
      <svg class="key" width="16" height="26"><use href="#icon-key"/></svg>********
    </div>
    <div class="field" style="left:20px;top:284px;width:265px;">
      <svg class="key" width="16" height="26"><use href="#icon-key"/></svg>********
    </div>
    <div class="check" style="left:235px;top:225px;width:68px;height:68px;">
      <span><svg width="30" height="26"><use href="#icon-tick"/></svg></span>
    </div>
    <div class="ground-line"></div>
    <div class="login-button"><span class="mark"></span>Login with Linkora</div>
  </section>

  <section class="screen screen--login">
    <div class="backdrop" role="img" aria-label="Dim photo of a football pitch with a player kicking"></div>
    <header class="status-bar">
      <svg class="signal" width="20" height="8"><use href="#icon-signal"/></svg>
      9:00 AM
      <svg class="battery" width="20" height="9"><use href="#icon-battery"/></svg>
    </header>
    <div class="wordmark">goalminded</div>
    <div class="welcome" style="top:159px;">Welcome</div>
    <div class="field" style="left:14px;top:193px;width:265px;">
      <svg width="28" height="24"><use href="#icon-mail"/></svg>anders@postvik.com
    </div>
    <div class="field" style="left:14px;top:237px;width:265px;">
      <svg class="key" width="16" height="26"><use href="#icon-key"/></svg>********
    </div>
    <div class="check" style="left:251px;top:205px;width:62px;height:62px;">
      <span><svg width="28" height="24"><use href="#icon-tick"/></svg></span>
    </div>
    <div class="ground-line"></div>
    <div class="login-button"><span class="mark"></span>Login with Linkora</div>
  </section>

</main>
</body>
</html>
```